Create our new Brightcup Coffee Syrup Label designs. A delicious job!

Design a front label for a range of coffee syrup flavours. The brand is 'Brightcup Coffee Syrups'. The flavours, vanilla, hazelnut and caramel.
Our coffee syrups are made with only natural colours and flavours and are positioned in the popular premium space in Australian and international cafes.
The labels will be applied to 750 ml Boston Bottles (see attached image).
Given that coffee syrups are often positioned in high visibility locations in cafes, they can be considered as objects of functional beauty.
This range is a sub brand for our company and I have attached our main brand images in the flavours we want. we want this brand to look different to this Marlowe branded range, but included the image to show what we are currently doing in this space.
The different flavours can be identified by a combination of colour and text, which may be a line or section of the otherwise same overall design.
We are going to do a 2 part label with the front just carrying Brand and flavour descriptors plus 750 ml.
Total Bottle height is 240 mm bottle width is 70 mm

Target Market(s)

Cafe patrons, primarily women, 18-35, Middle class in terms of economics, regular cafe patrons. Who are looking for a guilt free treat in their busy day.

Logo Text

Brightcup Coffee Syrups Vanilla (or Hazelnut, or Caramel) 750 ml

Logo styles of interest
Pictorial/Combination Logo
Font styles to use
Sans Serif

Colors

Designer to choose colors to be used in the design.

Requirements
Must have
• A clear design, which is a combination of font and image. it needs to be legible from up to 2m away (across a counter in a cafe).
• We would like to see a device, which may be a gold drop, that may be the 'brightcup' meant to the coffee.
• The way our coffee syrups are used is by adding a small amount (15 ml) to a cup
• of coffee, this adds both flavour and sweetness to the overall coffee experience, and cafes charge a premium for this service. We want our package to show this will be a great thing to do.
• We have a few options in terms of Label stock. We can print on a foil, that will allow a metallic sheen to come through the colours (see example of the Marlowe branded bottles.
Nice to have
• We are looking for a modern, clean and distinctive look and feel to this range.
• I have added a key line for the front and back label, however we can create a different label die line should the design warrant that. Note this is just for the front label.
Should not have
• Difficult to read fonts or imagery that is not clear.
• Should look different to the Marlowe branded product range.

```html
<!DOCTYPE html>
<html lang="en">
<head>
<meta charset="utf-8">
<title>Brightcup Coffee Syrup Labels</title>
<link rel="stylesheet" href="https://fonts.googleapis.com/css2?family=Comfortaa:wght@500&family=PT+Sans+Narrow&display=swap">
<style>
  :root {
    --page: #ffffff;
    --label-bg: #231f20;
    --label-edge: #1a1718;
    --brand-ink: #ffffff;
    --band-ink: #2a2224;
    --hazel-dark: #8a4a1c;
    --hazel-mid: #c98a55;
    --hazel-light: #f3d7b8;
    --vanilla-dark: #8f8c8e;
    --vanilla-mid: #c9c7c8;
    --vanilla-light: #f7f6f6;
    --caramel-dark: #c99a1e;
    --caramel-mid: #e8c350;
    --caramel-light: #fff2b8;
  }
  * { margin: 0; padding: 0; box-sizing: border-box; }
  html, body { width: 1200px; height: 1200px; overflow: hidden; background: var(--page); }
  .canvas { position: relative; width: 1200px; height: 1200px; }

  .label {
    position: absolute;
    top: 346px;
    width: 319px;
    height: 498px;
    background: var(--label-bg);
    border: 2px solid var(--label-edge);
    overflow: hidden;
  }
  .label--hazelnut { left: 58px; }
  .label--vanilla { left: 430px; }
  .label--caramel { left: 809px; }

  .brand-name {
    position: absolute;
    top: 42px;
    left: 0;
    width: 100%;
    text-align: center;
    font-family: "Comfortaa", sans-serif;
    font-weight: 500;
    font-size: 54px;
    letter-spacing: -1px;
    color: var(--brand-ink);
  }

  .drop-device {
    position: absolute;
    left: 50%;
    top: 236px;
    width: 230px;
    height: 230px;
    transform: translate(-50%, -50%);
    border-radius: 50%;
  }
  .label--hazelnut .drop-device { background: radial-gradient(circle, var(--hazel-mid) 0%, rgba(201,138,85,0.45) 28%, rgba(255,255,255,0.12) 48%, rgba(35,31,32,0) 70%); }
  .label--vanilla .drop-device { background: radial-gradient(circle, var(--vanilla-mid) 0%, rgba(201,199,200,0.45) 28%, rgba(255,255,255,0.12) 48%, rgba(35,31,32,0) 70%); }
  .label--caramel .drop-device { background: radial-gradient(circle, var(--caramel-mid) 0%, rgba(232,195,80,0.45) 28%, rgba(255,255,255,0.12) 48%, rgba(35,31,32,0) 70%); }

  .flavour {
    position: absolute;
    top: 352px;
    left: 0;
    width: 100%;
    text-align: center;
    font-family: "Comfortaa", sans-serif;
    font-weight: 500;
    font-size: 46px;
    letter-spacing: -1px;
    -webkit-background-clip: text;
    background-clip: text;
    color: transparent;
  }
  .label--hazelnut .flavour { background-image: linear-gradient(90deg, var(--hazel-dark), var(--hazel-mid), var(--hazel-dark)); }
  .label--vanilla .flavour { background-image: linear-gradient(90deg, var(--vanilla-light), var(--vanilla-mid), var(--vanilla-light)); }
  .label--caramel .flavour { background-image: linear-gradient(90deg, var(--caramel-light), var(--caramel-mid), var(--caramel-light)); }

  .product-band {
    position: absolute;
    left: 3px;
    right: 3px;
    top: 446px;
    height: 46px;
    display: flex;
    align-items: center;
    justify-content: center;
    font-family: "PT Sans Narrow", sans-serif;
    font-size: 25px;
    color: var(--band-ink);
  }
  .label--hazelnut .product-band { background: linear-gradient(100deg, var(--hazel-dark) 0%, var(--hazel-mid) 25%, var(--hazel-light) 55%, var(--hazel-mid) 80%, var(--hazel-dark) 100%); }
  .label--vanilla .product-band { background: linear-gradient(100deg, var(--vanilla-dark) 0%, var(--vanilla-mid) 25%, var(--vanilla-light) 55%, var(--vanilla-mid) 80%, var(--vanilla-dark) 100%); }
  .label--caramel .product-band { background: linear-gradient(100deg, var(--caramel-dark) 0%, var(--caramel-mid) 25%, var(--caramel-light) 55%, var(--caramel-mid) 80%, var(--caramel-dark) 100%); }
</style>
</head>
<body>
<main class="canvas">
  <section class="label label--hazelnut">
    <h2 class="brand-name">Brightcup</h2>
    <div class="drop-device" role="img" aria-label="Copper metallic drop device with spiral on a soft glow"></div>
    <p class="flavour">Hazlenut</p>
    <p class="product-band">Coffee Syrup</p>
  </section>

  <section class="label label--vanilla">
    <h2 class="brand-name">Brightcup</h2>
    <div class="drop-device" role="img" aria-label="Silver metallic drop device with spiral on a soft glow"></div>
    <p class="flavour">Vanilla</p>
    <p class="product-band">Coffee Syrup</p>
  </section>

  <section class="label label--caramel">
    <h2 class="brand-name">Brightcup</h2>
    <div class="drop-device" role="img" aria-label="Gold metallic drop device with spiral on a soft glow"></div>
    <p class="flavour">Caramel</p>
    <p class="product-band">Coffee Syrup</p>
  </section>
</main>
</body>
</html>
```